custom carpentry, woodworking and home repair company needs logo design and business card design

Attention: I apologize but I just received notification from my state that I cannot use the company name that I originally submitted (Beyond The Bench). The new name will be Joinolux We need a company logo and business card design for our new company based in the Hampton Roads area of Virginia. The company name is Joinolux. The final design should give a first impression of true craftsmanship and attention to detail. We would like the card to include the company name, my name Mark Tellman (owner), phone number (757) 348-2615, website (joinolux-example.com) and email address (mark@joinolux-example.com). Everything else is up to your discretion. Thanks, have fun, and good luck.

Industry/Entity Type

Business

Contact Information for Business Card

See project description

Logo Text

see project description

Colors

Designer to choose colors to be used in the design.

```html
<!DOCTYPE html>
<html lang="en">
<head>
<meta charset="utf-8">
<title>Joinolux — Business Card</title>
<link rel="stylesheet" href="https://fonts.googleapis.com/css2?family=Arimo:wght@400;700&display=swap">
<style>
  :root {
    --teal: #4d7c74;
    --charcoal: #3b3b3c;
    --silver: #a9aaab;
    --grey-text: #8c8d8e;
    --paper: #ffffff;
    --backdrop: #ecebe8;
    --pale: #e4e6e5;
  }
  * { box-sizing: border-box; margin: 0; padding: 0; }
  html, body { width: 1200px; height: 1000px; overflow: hidden; }
  body {
    background: var(--backdrop);
    font-family: "Arimo", Arial, sans-serif;
    display: flex;
    flex-direction: column;
    align-items: center;
    justify-content: center;
    gap: 40px;
  }
  .card {
    position: relative;
    width: 770px;
    height: 440px;
    overflow: hidden;
    box-shadow: 0 6px 18px rgba(0,0,0,0.18);
  }
  .card-art { position: absolute; inset: 0; width: 100%; height: 100%; }

  /* Front */
  .card-front { background: var(--paper); }
  .contact-list {
    position: absolute;
    top: 26px;
    right: 26px;
    list-style: none;
    display: flex;
    flex-direction: column;
    align-items: flex-end;
    gap: 10px;
  }
  .contact-item {
    display: flex;
    align-items: center;
    gap: 8px;
    height: 26px;
    padding: 0 10px 0 30px;
    background: var(--charcoal);
    clip-path: polygon(16px 0, 100% 0, 100% 100%, 0 100%);
    color: var(--paper);
    font-size: 13px;
    letter-spacing: 0.2px;
  }
  .contact-icon {
    width: 18px; height: 18px;
    border: 1.5px solid var(--paper);
    border-radius: 50%;
    display: flex; align-items: center; justify-content: center;
  }
  .contact-icon svg { width: 10px; height: 10px; }

  .brand-front {
    position: absolute;
    left: 40px;
    top: 150px;
    display: flex;
    align-items: center;
    gap: 8px;
    color: var(--teal);
    font-size: 22px;
    font-weight: 700;
  }
  .brand-mark { width: 16px; height: 16px; background: var(--teal); }

  .person {
    position: absolute;
    left: 170px;
    top: 186px;
    text-align: right;
  }
  .person-name {
    color: var(--teal);
    font-size: 44px;
    font-weight: 700;
    letter-spacing: 0.5px;
    line-height: 1.05;
  }
  .person-role {
    color: var(--grey-text);
    font-size: 24px;
    font-weight: 400;
    line-height: 1.1;
    margin-top: 4px;
    margin-right: 4px;
  }

  /* Back */
  .card-back { background: var(--teal); }
  .brand-back {
    position: absolute;
    left: 0; right: 0;
    top: 120px;
    display: flex;
    flex-direction: column;
    align-items: center;
    color: var(--pale);
  }
  .brand-back-name {
    display: flex;
    align-items: center;
    gap: 12px;
    font-size: 46px;
    font-weight: 700;
    letter-spacing: 1px;
  }
  .brand-back .brand-mark { width: 26px; height: 26px; background: var(--pale); }
  .brand-back-site {
    margin-top: 8px;
    font-size: 14px;
    letter-spacing: 5px;
  }
</style>
</head>
<body>

  <section class="card card-front" aria-label="Business card front">
    <svg class="card-art" viewBox="0 0 770 440" preserveAspectRatio="none" aria-hidden="true">
      <path fill="var(--teal)" d="M0,392 C180,374 380,368 580,378 L560,440 L0,440 Z"/>
      <path fill="var(--charcoal)" d="M770,96 C650,160 570,290 540,440 L770,440 Z"/>
      <path fill="var(--paper)" d="M40,376 C280,318 540,282 770,254 L770,264 C540,290 300,326 40,376 Z"/>
      <path fill="var(--silver)" d="M60,368 C300,312 540,282 770,262 L770,288 C540,302 320,330 60,368 Z"/>
    </svg>

    <ul class="contact-list">
      <li class="contact-item">(757) 348-2615
        <span class="contact-icon"><svg viewBox="0 0 10 10"><rect x="2.5" y="0.5" width="5" height="9" rx="1" fill="none" stroke="#fff" stroke-width="1.2"/></svg></span>
      </li>
      <li class="contact-item">joinolux-example.com
        <span class="contact-icon"><svg viewBox="0 0 10 10"><circle cx="5" cy="5" r="4" fill="none" stroke="#fff" stroke-width="1.2"/><path d="M1,5 H9 M5,1 C3,3 3,7 5,9 C7,7 7,3 5,1" fill="none" stroke="#fff" stroke-width="0.9"/></svg></span>
      </li>
      <li class="contact-item">mark@joinolux-example.com
        <span class="contact-icon"><svg viewBox="0 0 10 10"><rect x="0.8" y="2" width="8.4" height="6" fill="none" stroke="#fff" stroke-width="1.2"/><path d="M1,2.3 L5,5.6 L9,2.3" fill="none" stroke="#fff" stroke-width="1.1"/></svg></span>
      </li>
    </ul>

    <div class="brand-front"><span class="brand-mark"></span>Joinolux</div>

    <div class="person">
      <p class="person-name">Mark Tellman</p>
      <p class="person-role">Owner</p>
    </div>
  </section>

  <section class="card card-back" aria-label="Business card back">
    <svg class="card-art" viewBox="0 0 770 440" preserveAspectRatio="none" aria-hidden="true">
      <path fill="var(--paper)" d="M0,290 C260,282 500,330 650,440 L610,440 C470,350 250,306 0,304 Z"/>
    </svg>
    <div class="brand-back">
      <p class="brand-back-name"><span class="brand-mark"></span>Joinolux</p>
      <p class="brand-back-site">joinolux-example.com</p>
    </div>
  </section>

</body>
</html>
```